Simple menu needed for Asian food truck

We are an Asian food truck that attends big festivals. Our menu is very simple featuring only about 5 or 6 dishes, but we need big pictures and lettering to capture the attention of festival goers. Our motto is "Fresh, Authentic, Homemade", it would be great to include that somewhere. We also need a menu that possibly magnetic so that we can easily take off items that are sold out, change pricing or add different dishes for specific venues. Attached is an example of what our current menu looks like.

```html
<!DOCTYPE html>
<html lang="en">
<head>
<meta charset="utf-8">
<title>Mei's Authentic Egg Rolls – Menu</title>
<link href="https://fonts.googleapis.com/css2?family=Oswald:wght@400;500;600&family=Open+Sans:wght@400&display=swap" rel="stylesheet">
<style>
  :root {
    --page: #e8e5df;
    --cream: #f8f1e1;
    --ink: #1f2129;
    --gold: #f1bd4f;
    --gold-deep: #e8a93a;
    --orange: #d9772a;
    --title: #3b3b3d;
    --price-text: #f2c23d;
    --white: #ffffff;
    --card: #d9dde3;
    --tray: #f4f1ea;
    --eggroll: #d9a25a;
    --wing: #e2b54e;
    --spring: #f2d9cf;
    --bbq: #8f2a2e;
    --tea: #ef8a4a;
    --rice: #d8b77a;
  }
  * { box-sizing: border-box; margin: 0; padding: 0; }
  html, body { width: 1199px; height: 1200px; overflow: hidden; }
  body { background: var(--page); position: relative; font-family: "Open Sans", sans-serif; }

  .menu { position: absolute; left: 175px; top: 15px; width: 850px; height: 1170px; box-shadow: 0 6px 24px rgba(0,0,0,.18); }
  .menu-bg { position: absolute; inset: 0; }

  .menu-title { position: absolute; left: 42px; top: 32px; font-family: "Oswald", sans-serif; font-weight: 400; font-size: 44px; letter-spacing: .5px; color: var(--title); }

  .brand { position: absolute; right: 40px; top: 86px; display: flex; align-items: center; gap: 12px; font-family: "Oswald", sans-serif; font-weight: 600; font-size: 34px; color: var(--orange); }
  .brand-dot { width: 34px; height: 34px; border-radius: 50%; border: 3px solid var(--orange); }

  .item { position: absolute; width: 290px; text-align: center; color: var(--white); }
  .item-photo { position: relative; width: 240px; height: 205px; margin: 0 auto; border-radius: 48% 52% 44% 56% / 56% 46% 54% 44%; background: radial-gradient(circle at 45% 40%, var(--gold) 0%, var(--gold-deep) 100%); overflow: hidden; }
  .item-photo .dish { position: absolute; left: -6%; right: -10%; top: 22%; bottom: 18%; border-radius: 10px; }
  .dish-eggroll { background: radial-gradient(ellipse at 50% 50%, var(--eggroll) 0%, var(--eggroll) 38%, var(--tray) 62%, var(--tray) 100%); }
  .dish-wing { background: radial-gradient(ellipse at 55% 50%, var(--wing) 0%, var(--rice) 45%, var(--tray) 68%, var(--tray) 100%); }
  .dish-spring { background: radial-gradient(ellipse at 50% 50%, var(--spring) 0%, #f6e7df 45%, var(--tray) 70%, var(--tray) 100%); }
  .dish-bbq { background: radial-gradient(ellipse at 50% 48%, var(--bbq) 0%, #a83a3a 40%, var(--tray) 66%, var(--tray) 100%); }
  .dish-tea { background: linear-gradient(90deg, #e8626a 0%, var(--tea) 50%, #f2c454 100%); left: 12%; right: 8%; top: 10%; bottom: 14%; border-radius: 8px; }
  .dish-rice { background: radial-gradient(ellipse at 50% 50%, var(--rice) 0%, #cfa86a 42%, var(--tray) 68%, var(--tray) 100%); }
  .price-badge { position: absolute; width: 100px; height: 100px; border-radius: 50%; background: var(--orange); border: 3px solid var(--cream); box-shadow: 0 3px 8px rgba(0,0,0,.35); display: flex; flex-direction: column; align-items: center; justify-content: center; font-family: "Oswald", sans-serif; color: var(--white); }
  .price-badge .amount { font-size: 40px; font-weight: 600; line-height: 1; }
  .price-badge .unit { font-size: 13px; font-weight: 400; margin-top: 2px; }
  .item-name { margin-top: 52px; font-family: "Oswald", sans-serif; font-weight: 600; font-size: 30px; line-height: 1.1; letter-spacing: .3px; white-space: nowrap; }
  .item-note { font-size: 15px; line-height: 1.35; margin-top: 4px; }
  .item-deal { font-family: "Oswald", sans-serif; font-weight: 500; font-size: 24px; color: var(--price-text); margin-top: 4px; }

  .socials { position: absolute; left: 40px; top: 1040px; display: flex; gap: 16px; }
  .social-dot { width: 42px; height: 42px; border-radius: 50%; border: 2px solid var(--orange); }
  .cards { position: absolute; left: 30px; top: 1100px; display: flex; gap: 8px; }
  .card-chip { width: 74px; height: 42px; border-radius: 5px; background: var(--card); box-shadow: 0 1px 3px rgba(0,0,0,.25); }
</style>
</head>
<body>
<main class="menu">
  <svg class="menu-bg" viewBox="0 0 850 1170" width="850" height="1170" aria-hidden="true">
    <rect width="850" height="1170" fill="var(--cream)"/>
    <path fill="var(--ink)" d="M0 175 C40 110 90 96 160 100 C260 106 330 72 430 90 C520 108 565 170 645 200 C725 230 790 248 850 238 L850 1170 L715 1170 C700 1120 660 1108 600 1106 C480 1102 400 1078 300 1040 C200 1002 100 988 0 1008 Z"/>
  </svg>

  <h1 class="menu-title">MEI'S AUTHENTIC EGG ROLLS</h1>
  <div class="brand"><span class="brand-dot"></span><span>MEI'S EGG ROLLS</span></div>

  <section class="item" style="left:8px; top:250px;">
    <div class="item-photo" role="img" aria-label="Photo of three chicken egg rolls in a paper tray"><span class="dish dish-eggroll"></span></div>
    <div class="price-badge" style="left:180px; top:150px;"><span class="amount">$6</span><span class="unit">3 FOR $6</span></div>
    <h2 class="item-name">CHICKEN EGGROLLS</h2>
    <p class="item-deal">3 FOR $6</p>
  </section>

  <section class="item" style="left:280px; top:280px;">
    <div class="item-photo" role="img" aria-label="Photo of a stuffed chicken wing with fried rice"><span class="dish dish-wing"></span></div>
    <div class="price-badge" style="left:180px; top:150px;"><span class="amount">$8</span><span class="unit">COMBO</span></div>
    <h2 class="item-name">ANGEL WING</h2>
    <p class="item-note">(Stuffed Chicken Wing)<br>with side of fried rice</p>
  </section>

  <section class="item" style="left:552px; top:305px;">
    <div class="item-photo" role="img" aria-label="Photo of fresh shrimp spring rolls in a paper tray"><span class="dish dish-spring"></span></div>
    <div class="price-badge" style="left:180px; top:150px;"><span class="amount">$6</span><span class="unit">2 FOR $6</span></div>
    <h2 class="item-name">FRESH SPRINGROLLS</h2>
    <p class="item-note">(Shrimp or Veggie)</p>
    <p class="item-deal">2 FOR $6</p>
  </section>

  <section class="item" style="left:8px; top:640px;">
    <div class="item-photo" role="img" aria-label="Photo of Chinese barbecue pork skewers"><span class="dish dish-bbq"></span></div>
    <div class="price-badge" style="left:180px; top:150px;"><span class="amount">$6</span><span class="unit">2 FOR $6</span></div>
    <h2 class="item-name">CHINESE BBQ PORK</h2>
    <p class="item-note">Skewers</p>
    <p class="item-deal">2 FOR $6</p>
  </section>

  <section class="item" style="left:280px; top:665px;">
    <div class="item-photo" role="img" aria-label="Photo of three glasses of flavored iced tea"><span class="dish dish-tea"></span></div>
    <div class="price-badge" style="left:180px; top:150px;"><span class="amount">$5</span><span class="unit">GLASS</span></div>
    <h2 class="item-name">FLAVORED TEA</h2>
    <p class="item-note">Strawberry, Mango<br>or Peach</p>
  </section>

  <section class="item" style="left:552px; top:690px;">
    <div class="item-photo" role="img" aria-label="Photo of fried rice in a paper tray"><span class="dish dish-rice"></span></div>
    <div class="price-badge" style="left:180px; top:150px;"><span class="amount">$5</span><span class="unit">BOWL</span></div>
    <h2 class="item-name">FRIED RICE</h2>
    <p class="item-note">(Chicken or Pork)</p>
  </section>

  <div class="socials">
    <span class="social-dot"></span><span class="social-dot"></span><span class="social-dot"></span>
  </div>
  <div class="cards">
    <span class="card-chip"></span><span class="card-chip"></span><span class="card-chip"></span><span class="card-chip"></span>
  </div>
</main>
</body>
</html>
```